Wedding Invitation : Who helps to design a chic wedding card?

We need a chic invitation design for our wedding invitations.

FRONT

- Name logo : Mira & Joost
- Wedding date : zaterdag 9 juli 2022
- Quote : forever starts here

BACK

- Wij geven elkaar het ja-woord op zaterdag 9 juli 2022
Translation: We’ll say yes on Saturday 9th of July 2022 in the church of Wendelkouter
- Timeline with icons:

o JAWOORD (Translation: We say yes)
o 15u00

o RECEPTIE (Translation: Reception)
o 18u30

o DINER (Translation: Dinner)
o 19u30
o Feestzaal Lorvendaal (Location)

o FEEST (Translation: Dinner)
o 21u30

- Locations:

o Icon of a church:
Wendelkouter
o Icon of a location:
Feestzaal Lorvendaal
Burgemeester Tijskenslaan 47B
9871 Olmsveke

- RSVP Gelieve jouw aanwezigheid te bevestigen voor 29 mei 2022
(Translation: Please confirm before 29th of May 2022)

STYLE:

- Rosé gold relief press symbols
- Font style : handwritten or serif name (eg. playfair display)
- Font style: description in a more minimalistic font
- Cards will be in craft or ivory white, text will be in rosé gold relief press or black print

FORMAT
American format (229mm W x 114 mm H)

Target Market(s)

People 25-40 years old

Industry/Entity Type

Wedding / Event

Font styles to use
Serif
Sans Serif
Script

Colors

Designer to choose colors to be used in the design.

Requirements
Must have
• Name logo
Nice to have
• Minimalistic animation / icons
Should not have
• Jungle prints

```html
<!DOCTYPE html>
<html lang="nl">
<head>
<meta charset="utf-8">
<title>Mira &amp; Joost – Huwelijksuitnodiging</title>
<link rel="stylesheet" href="https://fonts.googleapis.com/css2?family=Archivo:wght@400;500;600&family=Parisienne&display=swap">
<style>
  :root {
    --backdrop: #dcdfe1;
    --paper: #f7f7f6;
    --rose-gold: #d8957a;
    --rose-gold-deep: #b9735c;
    --ink: #1f1f1f;
    --ink-soft: #3a3a3a;
  }
  * { box-sizing: border-box; margin: 0; padding: 0; }
  html, body {
    width: 1200px; height: 900px; overflow: hidden;
    background: var(--backdrop);
    font-family: "Archivo", Arial, sans-serif;
    color: var(--ink);
  }
  .card {
    position: absolute;
    left: 200px;
    width: 800px; height: 398px;
    background: var(--paper);
    box-shadow: 0 2px 6px rgba(0,0,0,.08);
  }
  .card--back { top: 32px; }
  .card--front { top: 470px; }

  /* ---------- back side ---------- */
  .name-mark {
    position: absolute;
    color: var(--rose-gold);
    font-weight: 500;
    letter-spacing: .18em;
    text-transform: uppercase;
    white-space: nowrap;
  }
  .card--back .name-mark {
    top: 40px; left: 0; width: 100%; text-align: center; font-size: 11px;
  }
  .headline {
    position: absolute; top: 64px; left: 0; width: 100%;
    text-align: center;
    font-size: 13px; font-weight: 500; letter-spacing: .14em;
    text-transform: uppercase;
  }
  .timeline {
    position: absolute; top: 122px; left: 110px;
    list-style: none;
  }
  .timeline__item {
    display: flex; align-items: flex-start; gap: 14px;
    margin-bottom: 14px;
  }
  .icon { width: 30px; height: 30px; flex: none; }
  .icon * { fill: none; stroke: var(--rose-gold); stroke-width: 1.4; stroke-linecap: round; stroke-linejoin: round; }
  .timeline__text, .venue__text {
    font-size: 10.5px; line-height: 1.3; letter-spacing: .06em;
  }
  .timeline__label { text-transform: uppercase; font-weight: 500; }
  .venues {
    position: absolute; top: 122px; left: 470px;
    list-style: none;
  }
  .venue { display: flex; align-items: flex-start; gap: 14px; margin-bottom: 26px; }
  .rsvp {
    position: absolute; bottom: 44px; right: 70px;
    font-size: 9.5px; letter-spacing: .08em; color: var(--ink-soft);
  }

  /* ---------- front side ---------- */
  .frame {
    position: absolute; inset: 34px 40px;
    border: 1px solid var(--rose-gold);
  }
  .frame::after {
    content: ""; position: absolute; inset: 3px;
    border: 1px solid var(--rose-gold);
    opacity: .55;
  }
  .card--front .name-mark {
    top: 130px; left: 0; width: 100%; text-align: center;
    font-size: 15px; color: var(--rose-gold-deep);
  }
  .couple {
    position: absolute; top: 176px; left: 0; width: 100%;
    text-align: center;
    font-size: 28px; font-weight: 400; letter-spacing: .12em;
    text-transform: uppercase;
  }
  .date {
    position: absolute; top: 222px; left: 0; width: 100%;
    text-align: center;
    font-size: 12px; font-weight: 600; letter-spacing: .16em;
    text-transform: uppercase;
  }
  .quote {
    position: absolute; right: 64px; bottom: 58px;
    font-family: "Parisienne", cursive;
    font-size: 20px; color: var(--ink-soft);
  }
</style>
</head>
<body>

<section class="card card--back" aria-label="Achterzijde uitnodiging">
  <div class="name-mark">Mira &amp; Joost</div>
  <h1 class="headline">Wij geven elkaar het ja-woord op zaterdag 9 juli 2022</h1>

  <ul class="timeline">
    <li class="timeline__item">
      <svg class="icon" viewBox="0 0 30 30" aria-hidden="true"><circle cx="11" cy="16" r="7"/><circle cx="19" cy="16" r="7"/></svg>
      <div class="timeline__text"><div class="timeline__label">Jawoord</div><div>15u00</div></div>
    </li>
    <li class="timeline__item">
      <svg class="icon" viewBox="0 0 30 30" aria-hidden="true"><path d="M8 5h6l-1 8a2 2 0 0 1-4 0zM11 15v9M8 24h6"/><path d="M17 5h6l-1 8a2 2 0 0 1-4 0zM20 15v9M17 24h6"/></svg>
      <div class="timeline__text"><div class="timeline__label">Receptie</div><div>18u30</div></div>
    </li>
    <li class="timeline__item">
      <svg class="icon" viewBox="0 0 30 30" aria-hidden="true"><circle cx="15" cy="15" r="8"/><circle cx="15" cy="15" r="5"/><path d="M4 6v18M3 6v4h2V6M26 6c-2 2-2 7 0 8v10"/></svg>
      <div class="timeline__text"><div class="timeline__label">Diner</div><div>19u30</div><div>Feestzaal Lorvendaal</div></div>
    </li>
    <li class="timeline__item">
      <svg class="icon" viewBox="0 0 30 30" aria-hidden="true"><rect x="5" y="19" width="20" height="6"/><rect x="8" y="13" width="14" height="6"/><rect x="11" y="8" width="8" height="5"/><path d="M15 8V4"/></svg>
      <div class="timeline__text"><div class="timeline__label">Feest</div><div>21u30</div><div>Feestzaal Lorvendaal</div></div>
    </li>
  </ul>

  <ul class="venues">
    <li class="venue">
      <svg class="icon" viewBox="0 0 30 30" aria-hidden="true"><path d="M15 3v4M13 5h4M9 13l6-6 6 6M9 13v13h12V13M4 26h22M4 26V17h5M26 26V17h-5M13 26v-5a2 2 0 0 1 4 0v5"/></svg>
      <div class="venue__text">Wendelkouter</div>
    </li>
    <li class="venue">
      <svg class="icon" viewBox="0 0 30 30" aria-hidden="true"><path d="M15 27s-8-8-8-14a8 8 0 0 1 16 0c0 6-8 14-8 14z"/><circle cx="15" cy="13" r="3"/></svg>
      <div class="venue__text">Feestzaal Lorvendaal<br>Burgemeester Tijskenslaan 47B<br>9871 Olmsveke</div>
    </li>
  </ul>

  <p class="rsvp">Gelieve jouw aanwezigheid te bevestigen voor 29 mei 2022</p>
</section>

<section class="card card--front" aria-label="Voorzijde uitnodiging">
  <div class="frame"></div>
  <div class="name-mark">Mira &amp; Joost</div>
  <h2 class="couple">Mira &amp; Joost</h2>
  <p class="date">Zaterdag 9 juli 2022</p>
  <p class="quote">forever starts here...</p>
</section>

</body>
</html>
```